eBook Cover Design for Healthy Recipes + recipe page

1. I am seeking a cover design for my ebook that contains healthy protein recipes plus I am seeking a design to display recipes in a visually attractive manner. Please refer to the attached images attached for inspo. The a4 cover design that I have done up needs to be enhanced so that the ebook looks really good and visually smoking hot! Please ensure you can provide a full editable working version of the file as the title may change so I need to be able to edit the file.

Brand: Falcon Maven
Book name: 18 Lean Fuel Power Plate Dishes

2. I am also seeking the design of an A4 recipe page see image attached as example.

Target Market(s)

Males and females that want to get in shape and want to find healthier options and ideas to make protein recipes.

Industry/Entity Type

Health And Wellness

Font styles to use
Other font styles liked:
• REFER TO IMAGES

Colors
f37122
f68e4e
f9ba93
fac994
faa54b
f78f20
fbc994
fbe7d2
fee3d5

Requirements
Must have
• Cover must contain logo and visually appealing, classy looking design. Must include title.

```html
<!DOCTYPE html>
<html lang="en">
<head>
<meta charset="utf-8">
<title>18 Lean Fuel Power Plate Dishes — Falcon Maven</title>
<link rel="stylesheet" href="https://fonts.googleapis.com/css2?family=Oswald:wght@700&family=Josefin+Sans:wght@300&family=Cinzel:wght@500&display=swap">
<style>
  :root {
    --cover-tan: #d8bb96;
    --ink-brown: #3d2f2a;
    --ink-dark: #2a2320;
  }
  * { margin: 0; padding: 0; box-sizing: border-box; }
  html, body { width: 849px; height: 1200px; overflow: hidden; background: var(--cover-tan); }
  .cover { position: relative; width: 849px; height: 1200px; background: var(--cover-tan); }
  .tile { position: absolute; }
  .c1 { left: 0; width: 277px; }
  .c2 { left: 285px; width: 278px; }
  .c3 { left: 570px; width: 279px; }
  .r1 { top: 0; height: 286px; }
  .r2 { top: 294px; height: 280px; }
  .r3 { top: 582px; height: 280px; }
  .photo-kale { background: radial-gradient(circle at 55% 40%, #5f7a2a, #3b4f1b 60%, #7a4a2a); }
  .photo-tea { background: radial-gradient(circle at 50% 50%, #b59a52, #e3e2d6 70%); }
  .photo-risotto { background: radial-gradient(circle at 60% 55%, #e0c06a, #d78a5b 45%, #eae4da 80%); }
  .photo-crepes { background: radial-gradient(circle at 50% 45%, #c7a386, #8a6a55 60%, #e9e3dc); }
  .photo-pancakes { background: radial-gradient(circle at 40% 55%, #9a6d52, #b58f76 45%, #ecebe8 75%); }
  .photo-pinkdrink { background: radial-gradient(circle at 45% 55%, #f0bfae, #e9c9c0 50%, #7f8a90); }
  .photo-smoothie { background: radial-gradient(circle at 55% 55%, #f3cfa2, #e5a56c 40%, #3a3a3d 75%); }
  .photo-infused { background: radial-gradient(circle at 50% 55%, #f1a24a, #d9d6cf 50%, #3a5a92 90%); }
  .number {
    position: absolute; left: 285px; top: 582px; width: 278px; height: 280px;
    display: flex; align-items: center; justify-content: center;
    font-family: "Oswald", "Arial Narrow", sans-serif; font-weight: 700;
    font-size: 330px; line-height: 1; color: var(--ink-brown); letter-spacing: -6px;
  }
  .title {
    position: absolute; left: 0; top: 880px; width: 849px; text-align: center;
    font-family: "Josefin Sans", "Helvetica Neue", sans-serif; font-weight: 300;
    font-size: 58px; line-height: 68px; color: var(--ink-dark); letter-spacing: 1px;
    text-transform: uppercase;
  }
  .brand {
    position: absolute; left: 0; top: 1090px; width: 849px; text-align: center;
    font-family: "Cinzel", Georgia, serif; font-weight: 500; color: var(--ink-dark);
  }
  .brand-name { font-size: 17px; letter-spacing: 7px; }
  .brand-byline { margin-top: 6px; font-size: 9px; letter-spacing: 5px; }
</style>
</head>
<body>
<main class="cover">
  <div class="tile c1 r1 photo-kale" role="img" aria-label="Baked kale chips in a wooden bowl"></div>
  <div class="tile c2 r1 photo-tea" role="img" aria-label="Two glass cups of herbal tea with mint and fennel"></div>
  <div class="tile c3 r1 photo-risotto" role="img" aria-label="Salmon risotto topped with shaved cheese and basil"></div>
  <div class="tile c1 r2 photo-crepes" role="img" aria-label="Rolled protein crepes with blueberries and mint"></div>
  <div class="tile c2 r2 photo-pancakes" role="img" aria-label="Folded protein pancakes with blueberries and a strawberry"></div>
  <div class="tile c3 r2 photo-pinkdrink" role="img" aria-label="Pink grapefruit drinks with mint"></div>
  <div class="tile c1 r3 photo-smoothie" role="img" aria-label="Peach smoothie in a glass jar with a striped straw"></div>
  <div class="number">18</div>
  <div class="tile c3 r3 photo-infused" role="img" aria-label="Orange and blueberry infused water in tall glasses"></div>
  <h1 class="title">Lean Fuel<br>Power Plate Dishes</h1>
  <div class="brand">
    <div class="brand-name">FALCON MAVEN</div>
    <div class="brand-byline">BY ELISE VARDEN</div>
  </div>
</main>
</body>
</html>
```